Oak Harbor Interiors Web Site

We are looking at web site for our start-up company which is located in Abu Dhabi United Arab Emirates. Our main business activity is Interior fit out for high medium to high end projects in residential, corporate and hospitality.
In terms of look and feel the web site should be vibrant yet professional reflecting the artistic/construction nature of our business and built along or allows the following aspects:
- Number of Pages: 8-10 main pages (Including 10 Sub Pages)
- A custom responsive web design compatible with all browsers
- Dynamic (admin panel). CMS
- Anti Spam Online Forms
- Photo & Video Gallery
- Mobile Ready (Iphone,Android)]
- Social Media Integration
- Google Map
- Banner Artworks

```html
<!DOCTYPE html>
<html lang="en">
<head>
<meta charset="utf-8">
<title>Oak Harbor Interiors</title>
<link rel="stylesheet" href="https://fonts.googleapis.com/css2?family=Open+Sans:ital,wght@0,400;0,600;0,700;1,400;1,600;1,700&family=Rokkitt:ital,wght@0,400;0,500;1,400;1,500&display=swap">
<style>
:root{
  --ink:#2b2b2b;
  --muted:#8a8a8a;
  --nav:#2f2f2f;
  --accent:#f0a51e;
  --blue:#1ea5e4;
  --teal:#2bb3ab;
  --orange:#f7a62a;
  --white:#ffffff;
}
*{box-sizing:border-box;margin:0;padding:0}
html,body{width:1200px;height:1000px;overflow:hidden;background:var(--white)}
body{position:relative;font-family:"Open Sans",Arial,sans-serif;color:var(--ink)}
.abs{position:absolute}
.top-band{left:0;top:0;width:1200px;height:222px;background:linear-gradient(#2e2e35,#15151a)}
.brand-plate{left:522px;top:6px;width:148px;height:54px;background:#18181c;display:flex;align-items:center;justify-content:center;z-index:3}
.brand-name{font-weight:700;font-size:9.5px;color:var(--accent);letter-spacing:.4px;white-space:nowrap}
.hero{left:155px;top:41px;width:876px;height:200px;display:flex}
.hero-slide{position:relative;width:50%;height:100%}
.hero-slide.light{background:linear-gradient(180deg,#f1f1f1 0%,#e2e2e2 55%,#f4f4f4 100%)}
.hero-slide.warm{background:linear-gradient(135deg,#6a4a33 0%,#c9a47a 40%,#b08a61 70%,#8f7357 100%)}
.hero-copy{position:absolute;left:38px;top:25px;font-family:"Rokkitt",Georgia,serif;line-height:1;white-space:nowrap}
.hero-copy .h{font-size:22px;letter-spacing:2.6px}
.hero-copy .s{font-style:italic;font-size:15px;letter-spacing:1.8px;margin-top:-2px}
.hero-copy .t{font-family:Georgia,serif;font-style:italic;font-size:10.5px;letter-spacing:.6px;margin-top:2px;line-height:12px}
.hero-slide.light .hero-copy{color:#222}
.hero-slide.warm .hero-copy{color:#fff}
.main-nav{left:155px;top:241px;width:876px;height:17px;background:var(--nav);font-size:7.5px;color:#ddd}
.main-nav a{color:inherit;text-decoration:none;position:absolute;top:4px;line-height:9px}
.main-nav a.active{color:var(--accent)}
.search{position:absolute;left:684px;top:3px;width:180px;height:11px;background:#1d1d1d;color:#777;font-size:6px;padding-left:8px;line-height:11px}
.search svg{position:absolute;right:6px;top:2px}
.tagline{left:0;width:1190px;top:284px;text-align:center;font-family:"Rokkitt",Georgia,serif;font-style:italic;font-weight:500;font-size:15px;letter-spacing:1.1px;line-height:12px;color:#222}
.section-title{left:0;width:1190px;text-align:center;font-style:italic;font-weight:400;font-size:18px;letter-spacing:1px;color:#222;line-height:22px}
.offer{width:270px;text-align:center}
.offer .icon{width:78px;height:38px;border-radius:50%;margin:0 auto;display:flex;align-items:center;justify-content:center}
.offer h3{font-weight:400;font-size:13px;margin-top:5px;line-height:16px}
.offer p{font-size:8.4px;line-height:11.3px;color:var(--muted);margin-top:2px;padding:0 2px}
.card{width:281px;height:136px;border:1px solid #efefef;text-align:center}
.card .photo{height:107px}
.card .title{font-size:10px;color:#555;margin-top:2px;line-height:12px}
.card .credit{font-size:6px;color:#777;margin-top:1px}
.card .credit b{color:#333}
.footer{left:0;top:848px;width:1200px;height:152px;background:linear-gradient(#1e1e24,#15151a)}
.fcol{top:862px;width:196px;font-size:8px;line-height:11.3px;color:#9a9a9a}
.fcol h4{color:var(--accent);font-size:10px;font-weight:700;margin-bottom:6px;line-height:12px}
.fcol .date{color:var(--accent)}
.fcol .news{color:#ddd}
.fcol .quote{font-style:italic}
.fcol .who{color:#fff;font-style:italic;font-weight:700}
.fcol.links li{list-style:none;color:#ddd;margin-bottom:2.4px}
.foot-rule{left:155px;top:976px;width:876px;height:1px;background:#2e2e35}
.copyright{left:155px;top:982px;font-size:8px;color:#ccc}
.copyright a{color:var(--accent);text-decoration:none;margin-left:8px}
.social{left:898px;top:983px;display:flex;gap:17px}
.social span{width:9px;height:9px;border-radius:50%;background:#555}
</style>
</head>
<body>
<div class="abs top-band"></div>
<div class="abs brand-plate"><span class="brand-name">OAK HARBOR INTERIORS</span></div>

<div class="abs hero">
  <div class="hero-slide light" role="img" aria-label="Photo: bright white living room with a grey sofa and colourful cushions">
    <div class="hero-copy"><div class="h">PRAESENT JUSTO</div><div class="s">SPRING / SUMMER 2014</div><div class="t">A wide selection of fine furniture!</div></div>
  </div>
  <div class="hero-slide warm" role="img" aria-label="Photo: close view of a beige sofa with patterned cushions">
    <div class="hero-copy"><div class="h">PRAESENT JUSTO</div><div class="s">NEW COLLECTION</div><div class="t">Style, comfort, quality, selection!<br>Think of us as your personal design assistant!</div></div>
  </div>
</div>

<nav class="abs main-nav">
  <a class="active" style="left:64px">HOME</a>
  <a style="left:156px">ABOUT US</a>
  <a style="left:269px">GALLERY</a>
  <a style="left:375px">BLOG</a>
  <a style="left:464px">SERVICES</a>
  <a style="left:571px">CONTACTS</a>
  <div class="search">Search<svg width="7" height="7" viewBox="0 0 10 10"><circle cx="4" cy="4" r="3" fill="none" stroke="#fff" stroke-width="1.5"/><line x1="6.2" y1="6.2" x2="9" y2="9" stroke="#fff" stroke-width="1.5"/></svg></div>
</nav>

<p class="abs tagline">We've been providing quality products and services to our residential and<br>commercial customers for over eighteen years.</p>

<h2 class="abs section-title" style="top:326px">WHAT WE OFFER</h2>

<div class="abs offer" style="left:161px;top:357px">
  <div class="icon" style="background:var(--blue)"><svg width="18" height="16" viewBox="0 0 18 16"><path d="M9 1 1 8h2v7h4v-5h4v5h4V8h2z" fill="#fff"/></svg></div>
  <h3>Space Planning</h3>
  <p>Lorem ipsum dolor sit amet, consectetuer adipiscing elit. Praesent vestibulum molestie lacus. Aenean nonummy hendrerit mauris. Phasellus porta. Fusce suscipit varius mi.</p>
</div>
<div class="abs offer" style="left:458px;top:357px">
  <div class="icon" style="background:var(--teal)"><svg width="18" height="14" viewBox="0 0 18 14"><rect x="3" y="1" width="12" height="9" rx="1" fill="none" stroke="#fff" stroke-width="1.5"/><rect x="1" y="11" width="16" height="2" fill="#fff"/></svg></div>
  <h3>3D Modeling</h3>
  <p>Lorem ipsum dolor sit amet, consectetuer adipiscing elit. Praesent vestibulum molestie lacus. Aenean nonummy hendrerit mauris. Phasellus porta. Fusce suscipit varius mi.</p>
</div>
<div class="abs offer" style="left:755px;top:357px">
  <div class="icon" style="background:var(--orange)"><svg width="18" height="14" viewBox="0 0 18 14"><rect x="1" y="1" width="16" height="12" fill="none" stroke="#fff" stroke-width="1.5"/><path d="M3 11l4-5 3 3 2-2 3 4z" fill="#fff"/><circle cx="13" cy="4.5" r="1.3" fill="#fff"/></svg></div>
  <h3>Paint and Color Selection</h3>
  <p>Lorem ipsum dolor sit amet, consectetuer adipiscing elit. Praesent vestibulum molestie lacus. Aenean nonummy hendrerit mauris. Phasellus porta. Fusce suscipit varius mi.</p>
</div>

<h2 class="abs section-title" style="top:494px">FEATURED PROJECTS</h2>

<div class="abs card" style="left:155px;top:525px"><div class="photo" role="img" aria-label="Photo: white bedroom with framed art" style="background:linear-gradient(#e9e9e9,#bdbdbd)"></div><div class="title">Lorem ipsum dolor sit amet</div><div class="credit">Design by <b>Marcus Hale</b></div></div>
<div class="abs card" style="left:452px;top:525px"><div class="photo" role="img" aria-label="Photo: two dark chairs against a pale wall on a wooden floor" style="background:linear-gradient(#e4d6cb 70%,#a85a40)"></div><div class="title">Lorem ipsum dolor sit amet</div><div class="credit">Design by <b>Nora Finch</b></div></div>
<div class="abs card" style="left:750px;top:525px"><div class="photo" role="img" aria-label="Photo: dining area with pendant lamps" style="background:linear-gradient(90deg,#d9cbb6,#ece6dc 60%,#c99a6a)"></div><div class="title">Lorem ipsum dolor sit amet</div><div class="credit">Design by <b>Marcus Hale</b></div></div>
<div class="abs card" style="left:155px;top:689px"><div class="photo" role="img" aria-label="Photo: bright living room with an armchair and curtains" style="background:linear-gradient(90deg,#ddd,#f2f2f2 50%,#b9b3aa)"></div><div class="title">Lorem ipsum dolor sit amet</div><div class="credit">Design by <b>Nora Finch</b></div></div>
<div class="abs card" style="left:452px;top:689px"><div class="photo" role="img" aria-label="Photo: bathroom with freestanding bathtub" style="background:linear-gradient(#e8e2da,#f1efec 60%,#d6cdc2)"></div><div class="title">Lorem ipsum dolor sit amet</div><div class="credit">Design by <b>Marcus Hale</b></div></div>
<div class="abs card" style="left:750px;top:689px"><div class="photo" role="img" aria-label="Photo: modern kitchen with wooden island" style="background:linear-gradient(#c7c27a,#eeeeea 40%,#a8713f)"></div><div class="title">Lorem ipsum dolor sit amet</div><div class="credit">Design by <b>Lena Park</b></div></div>

<footer class="abs footer"></footer>
<div class="abs fcol" style="left:155px"><h4>About Us</h4><p>Lorem ipsum dolor sit amet, consectetuer adipiscing elit. Praesent vestibulum molestie lacus. Aenean nonummy hendrerit mauris. Phasellus porta.<br>Fusce suscipit varius mi. Lorem ipsum dolor sit amet, consectetuer adipiscing</p></div>
<div class="abs fcol" style="left:378px;width:190px"><h4>Our News</h4><p class="date">2014-06-14</p><p class="news">Lorem ipsum dolor sit amet, consect etuer adipiscing elit.</p><p class="date" style="margin-top:6px">2014-06-14</p><p class="news">Lorem ipsum dolor sit amet, consect etuer adipiscing elit.</p></div>
<div class="abs fcol" style="left:601px;width:204px"><h4>Testimonials</h4><p class="quote">"Lorem ipsum dolor sit amet, consectetuer adipiscing elit. Aenean nonummy hendrerit mau."</p><p class="who">— Tom Reyes</p><p class="quote" style="margin-top:6px">"Lorem ipsum dolor sit amet, consectetuer adipiscing elit. Praesent vestibulum molese lacus. Aenean nonummy hendrerit mau."</p><p class="who">— Clara Moss</p></div>
<div class="abs fcol links" style="left:824px;width:210px"><h4>Useful Links</h4><ul><li>Donec in velit vel ipsum auctor pulvinar</li><li>Vestibulum iaculis lacinia est</li><li>Vestibulum iaculis lacinia est</li><li>Fusce euismod consequat ante</li><li>Lorem ipsum dolor sit amet</li><li>Consectetuer adipiscing elit</li></ul></div>
<div class="abs foot-rule"></div>
<p class="abs copyright">© 2014 All Rights Reserved &nbsp;|<a>Privacy Policy</a></p>
<div class="abs social"><span></span><span></span><span></span><span></span><span></span></div>
</body>
</html>
```